Business card design needed

see my website

www.calderwoodandpike.com

I am after a new logo and business card needs to fit in with the website. I like the look of typewriter text - would like this on the website as well if I could!

Industry/Entity Type

Business

Contact Information for Business Card

Calderwood and Pike
Design and Heritage Consultants

Marcia Dowell
Principal

+61 437 690 215
marcia@calderwoodandpike.com

www.calderwoodandpike.com

back of card

Interior Design
Consultancy on Period Home restoration and renovation
Heritage Impact Statements
Conservation Management Plans
Materials Conservation
Historical Research

```html
<!DOCTYPE html>
<html lang="en">
<head>
<meta charset="utf-8">
<title>Calderwood and Pike — Business Card</title>
<link rel="stylesheet" href="https://fonts.googleapis.com/css2?family=Courier+Prime:wght@400;700&display=swap">
<style>
  :root {
    --backdrop: #4a4a48;
    --card: #f3efe3;
    --card-edge: #dcd6c6;
    --teal: #2eb3a7;
    --ink: #55544f;
    --ink-dark: #2f2e2b;
    --type: "Courier Prime", "Courier New", monospace;
  }
  * { box-sizing: border-box; margin: 0; padding: 0; }
  html, body { width: 1200px; height: 1000px; overflow: hidden; }
  body {
    background: var(--backdrop);
    font-family: var(--type);
    color: var(--ink);
    position: relative;
  }
  .card {
    position: absolute;
    left: 220px;
    width: 760px;
    height: 434px;
    background: var(--card);
    border: 1px solid var(--card-edge);
    box-shadow: 0 10px 24px rgba(0,0,0,0.35);
  }
  .card--front { top: 48px; }
  .card--back { top: 518px; }

  .brand-name {
    font-family: var(--type);
    font-weight: 700;
    color: var(--teal);
    font-size: 40px;
    letter-spacing: 1px;
    text-transform: uppercase;
    line-height: 1;
  }
  .brand-tagline {
    font-family: var(--type);
    font-weight: 700;
    color: var(--ink);
    font-size: 20px;
    letter-spacing: 0.5px;
    margin-top: 10px;
  }

  /* Front */
  .card--front .brand {
    position: absolute;
    left: 56px;
    top: 150px;
  }
  .person {
    position: absolute;
    right: 54px;
    top: 44px;
    text-align: right;
  }
  .person__name {
    color: var(--teal);
    font-weight: 700;
    font-size: 20px;
  }
  .person__role {
    color: var(--ink);
    font-size: 17px;
    margin-top: 4px;
  }
  .contacts {
    position: absolute;
    left: 56px;
    bottom: 44px;
    list-style: none;
  }
  .contacts li {
    display: flex;
    align-items: center;
    gap: 10px;
    font-size: 15px;
    color: var(--ink);
    margin-top: 6px;
  }
  .contacts li.contacts__web {
    font-weight: 700;
    color: var(--ink-dark);
    font-size: 16px;
  }
  .contacts svg { width: 16px; height: 16px; flex: none; }

  /* Back */
  .card--back .brand {
    position: absolute;
    right: 54px;
    top: 58px;
    text-align: right;
  }
  .services {
    position: absolute;
    left: 56px;
    top: 190px;
    list-style: none;
  }
  .services li {
    font-size: 16px;
    color: var(--ink);
    line-height: 1.55;
  }
</style>
</head>
<body>

  <section class="card card--front" aria-label="Business card front">
    <div class="brand">
      <div class="brand-name">Calderwood and Pike</div>
      <div class="brand-tagline">Heritage &amp; Design Consultants</div>
    </div>

    <div class="person">
      <div class="person__name">Marcia Dowell</div>
      <div class="person__role">Principal</div>
    </div>

    <ul class="contacts">
      <li>
        <svg viewBox="0 0 16 16" aria-hidden="true">
          <circle cx="8" cy="8" r="7" fill="none" stroke="var(--teal)" stroke-width="1.3"/>
          <path d="M5.6 4.8 L6.8 4.6 L7.4 6.3 L6.6 7 Q7.3 8.6 9 9.4 L9.7 8.6 L11.4 9.2 L11.2 10.4 Q8.8 11.2 6.6 9.4 Q4.8 7.6 5.6 4.8 Z" fill="var(--teal)"/>
        </svg>
        +61 437 690 215
      </li>
      <li>
        <svg viewBox="0 0 16 16" aria-hidden="true">
          <circle cx="8" cy="8" r="7" fill="none" stroke="var(--teal)" stroke-width="1.3"/>
          <rect x="4.5" y="5.5" width="7" height="5" fill="none" stroke="var(--teal)" stroke-width="1.1"/>
          <path d="M4.5 5.5 L8 8.3 L11.5 5.5" fill="none" stroke="var(--teal)" stroke-width="1.1"/>
        </svg>
        marcia@calderwoodandpike.com
      </li>
      <li class="contacts__web">
        <svg viewBox="0 0 16 16" aria-hidden="true">
          <circle cx="8" cy="8" r="7" fill="none" stroke="var(--teal)" stroke-width="1.3"/>
          <circle cx="8" cy="8" r="3.6" fill="none" stroke="var(--teal)" stroke-width="1"/>
          <path d="M4.4 8 H11.6 M8 4.4 V11.6" stroke="var(--teal)" stroke-width="1"/>
        </svg>
        www.calderwoodandpike.com
      </li>
    </ul>
  </section>

  <section class="card card--back" aria-label="Business card back">
    <div class="brand">
      <div class="brand-name">Calderwood and Pike</div>
      <div class="brand-tagline">Heritage &amp; Design Consultants</div>
    </div>

    <ul class="services">
      <li>Consultancy on Period Home Restoration and Renovation</li>
      <li>Heritage Impact Statements</li>
      <li>Conservation Management Plans</li>
      <li>Interior Design</li>
      <li>Materials Conservation</li>
      <li>Historical Research</li>
      <li>Colour Styling</li>
    </ul>
  </section>

</body>
</html>
```